BRIVON - Business Card Design Project

We need a business card design for a consultant company called BRIVON, LLC. (stands for Bright Retail Inventory Venture Operations Network). The company provides Information Technology solutions, custom applications, services for financial and supply chain worldwide and focuses on business IT process improvements and all the steps leading to the procurement or integrating of any Enterprise related systems.

Industry/Entity Type

Financial

Requirements
Must have
• - In the submitted proposed version you should have one variant with black background and one with white.
The designer should show the shadow element of the company name in binary code (010000100101001001001001010101100100111101001110). It can be in one line or split in two

In your example please use the following info
Peter Dorne
Principal Consultant
pdorne@brivonhq.net
+1 (555) 014 - 2298

Please keep in mind that the design should have some spaces to add the second phone and/or web site name
Nice to have
• Since this IT company and is working closely with Accounting and Logistics Application you can add some elements (contour only) of these types of the bussines as well (for example some $ or euro sign or truck or warehouse element)
Should not have
• Don’t use any extra color that is not in the company color logo pattern

```html
<!DOCTYPE html>
<html lang="en">
<head>
<meta charset="utf-8">
<title>BRIVON Business Cards</title>
<link rel="stylesheet" href="https://fonts.googleapis.com/css2?family=Questrial&family=Arimo:wght@400;700&display=swap">
<style>
  :root {
    --backdrop: #d7dcde;
    --card-black: #050505;
    --card-white: #ffffff;
    --ink-white: #ffffff;
    --ink-black: #111111;
    --ink-grey: #4a4a4a;
    --binary-dark: #2e2e2e;
    --binary-light: #e6e6e6;
    --brand-blue: #1f8fd6;
    --card-shadow: 0 18px 40px rgba(0, 0, 0, 0.28);
  }
  * { box-sizing: border-box; margin: 0; padding: 0; }
  html, body {
    width: 1200px;
    height: 960px;
    overflow: hidden;
    background: var(--backdrop);
  }
  .sheet {
    position: relative;
    width: 1200px;
    height: 960px;
  }
  .card {
    position: absolute;
    left: 240px;
    width: 720px;
    height: 411px;
    box-shadow: var(--card-shadow);
    overflow: hidden;
  }
  .card--front { top: 50px; background: var(--card-black); }
  .card--back { top: 499px; background: var(--card-white); }

  .brand-dot {
    position: absolute;
    border-radius: 50%;
    background: var(--brand-blue);
  }
  .card--front .brand-dot { left: 62px; top: 112px; width: 150px; height: 150px; }
  .card--back .brand-dot { left: 150px; top: 44px; width: 80px; height: 80px; }

  .brand-name {
    position: absolute;
    font-family: "Questrial", sans-serif;
    font-weight: 400;
    letter-spacing: 6px;
    line-height: 1;
  }
  .card--front .brand-name {
    left: 236px; top: 112px;
    font-size: 96px;
    color: var(--ink-white);
  }
  .card--back .brand-name {
    left: 258px; top: 56px;
    font-size: 60px;
    color: var(--ink-black);
  }

  .tagline {
    position: absolute;
    left: 240px; top: 222px;
    font-family: "Arimo", sans-serif;
    font-weight: 700;
    font-size: 15.5px;
    color: var(--ink-white);
    white-space: nowrap;
  }

  .binary {
    position: absolute;
    left: 18px;
    bottom: 14px;
    width: 684px;
    height: 30px;
  }
  .binary text {
    font-family: "Arimo", sans-serif;
    font-size: 25px;
  }
  .card--front .binary text { fill: var(--binary-dark); }
  .card--back .binary text { fill: var(--binary-light); }

  .person {
    position: absolute;
    left: 0; right: 0;
    top: 160px;
    text-align: center;
    font-family: "Arimo", sans-serif;
  }
  .person__name {
    font-weight: 700;
    font-size: 25px;
    color: var(--ink-grey);
  }
  .person__role {
    font-family: "Questrial", sans-serif;
    font-size: 23px;
    color: var(--ink-grey);
    letter-spacing: 1px;
    margin-top: 2px;
  }

  .contacts {
    position: absolute;
    left: 90px; right: 40px;
    top: 272px;
    display: flex;
    justify-content: space-between;
    font-family: "Arimo", sans-serif;
    font-size: 15px;
    color: var(--ink-black);
  }
  .contacts__label { font-weight: 700; }
  .contacts__item--web { font-weight: 700; }
</style>
</head>
<body>
<main class="sheet">

  <section class="card card--front" aria-label="Business card, front">
    <span class="brand-dot" aria-hidden="true"></span>
    <h1 class="brand-name">BRIVON</h1>
    <p class="tagline">Bright Retail Inventory Venture Operations Network</p>
    <svg class="binary" viewBox="0 0 684 30" aria-label="BRIVON in binary">
      <text x="0" y="25" textLength="684" lengthAdjust="spacingAndGlyphs">010000100101001001001001010101100100111101001110</text>
    </svg>
  </section>

  <section class="card card--back" aria-label="Business card, back">
    <span class="brand-dot" aria-hidden="true"></span>
    <h2 class="brand-name">BRIVON</h2>
    <div class="person">
      <p class="person__name">Peter Dorne</p>
      <p class="person__role">Principal Consultant</p>
    </div>
    <div class="contacts">
      <span class="contacts__item"><span class="contacts__label">t:</span> +1 (555) 014 - 2298</span>
      <span class="contacts__item"><span class="contacts__label">e:</span> pdorne@brivonhq.net</span>
      <span class="contacts__item contacts__item--web">w: www.brivonhq.com</span>
    </div>
    <svg class="binary" viewBox="0 0 684 30" aria-label="BRIVON in binary">
      <text x="0" y="25" textLength="684" lengthAdjust="spacingAndGlyphs">010000100101001001001001010101100100111101001110</text>
    </svg>
  </section>

</main>
</body>
</html>
```